Pine Hollow Camp Brochure Design - TRI FOLD - See text examples added

Tri- Fold Brochure designed for Remote Alaskan Wilderness Fly-in lodge.We will provide several pictures. We want activities, directions, lodge rules, history, etc... We have provided our logo. Will work on adding text.
Looking for a professional, fun, adventurous feel.
Guests must fly in to the lodge. We are completely surrounded by wilderness. 33 miles from the nearest road. Take a 30 min flight seeing trip over mountains, glaciers, rivers and wildlife with Sky Tundrix to our private airstrip. Canoe in Heron Pond. See the Moose, Caribou, Bears, Lynx, wolves, and various birds. Go gold panning in the creeks.
Accommodations include your own private cabin with private bathroom. Access to the main lodge lounge and dining rooms, wood fired sauna, covered fire pit, and use of our canoe, life jackets, and rubber boots. Meals available. Wifi in main lodge. Movies in Theater.

Target Market(s)

Adventure, photographers, hikers, mountaineers, travelers

Industry/Entity Type

Tourism

Requirements
Must have
• Logo and pictures, information - Tri-Fold
Nice to have
• High quality attractive design with logo and information
Should not have
• Cartoony feel

```html
<!DOCTYPE html>
<html lang="en">
<head>
<meta charset="utf-8">
<title>Pine Hollow Camp – Tri-Fold Brochure</title>
<link rel="stylesheet" href="https://fonts.googleapis.com/css2?family=Graduate&family=Oswald:wght@300;400&family=Montserrat:wght@400;600;700;800&display=swap">
<style>
  :root{
    --red:#9b2335;
    --navy:#22324a;
    --orange:#e4541b;
    --ink:#3a3f47;
    --paper:#fbfaf7;
    --stage:#e4e4e2;
  }
  *{box-sizing:border-box;margin:0;padding:0}
  html,body{width:720px;height:1200px;overflow:hidden;background:var(--stage)}
  body{position:relative;font-family:"Montserrat",sans-serif;color:var(--ink)}
  .spread{position:absolute;left:10px;width:700px;height:540px;background:var(--paper);box-shadow:0 4px 14px rgba(0,0,0,.12);overflow:hidden}
  .spread--outside{top:40px}
  .spread--inside{top:620px;background:#fff}
  .spread-art{position:absolute;inset:0;width:700px;height:540px}
  .panel{position:absolute;top:0;width:233.33px;height:540px}
  .panel--left{left:0}
  .panel--middle{left:233.33px}
  .panel--right{left:466.66px}
  .fold{position:absolute;top:0;bottom:0;width:1px;background:rgba(0,0,0,.06)}

  .brand{display:flex;align-items:center;gap:6px;font-family:"Montserrat",sans-serif;font-weight:800;font-size:10px;letter-spacing:.04em;text-transform:uppercase;color:var(--navy)}
  .brand-dot{width:14px;height:14px;border-radius:50%;background:var(--red);flex:none}

  /* outside */
  .intro{position:absolute;left:20px;right:18px;top:26px;font-size:8px;line-height:1.55;text-align:justify}
  .intro p+p{margin-top:9px}
  .contact-brand{position:absolute;top:238px;left:0;right:0;display:flex;justify-content:center}
  .contact-card{position:absolute;left:0;bottom:40px;width:200px;height:130px;background:var(--navy);border-radius:0 34px 0 0;color:#fff;padding:26px 18px 0 22px}
  .contact-row{display:flex;align-items:flex-start;gap:8px;font-size:8px;line-height:1.35;margin-bottom:13px}
  .contact-row svg{width:11px;height:11px;flex:none}
  .cover-brand{position:absolute;top:20px;right:16px}
  .cover-title{position:absolute;left:22px;top:330px}
  .title-top{font-family:"Graduate",serif;font-size:27px;color:var(--navy);letter-spacing:.03em;line-height:1}
  .title-main{font-family:"Oswald",sans-serif;font-weight:300;font-size:29px;color:var(--red);line-height:1.02;text-transform:uppercase;margin-top:4px}
  .title-sub{font-family:"Montserrat",sans-serif;font-weight:600;font-size:9.5px;color:var(--navy);text-transform:uppercase;line-height:1.35;margin-top:8px;letter-spacing:.03em}
  .url-bar{position:absolute;right:0;bottom:16px;width:190px;height:28px;background:var(--red);border-radius:16px 0 0 0;color:#fff;font-size:9px;display:flex;align-items:center;padding-left:22px;letter-spacing:.02em}

  /* inside */
  .lead{position:absolute;left:18px;right:16px;top:22px}
  .lead-title{font-weight:800;font-size:8.5px;line-height:1.3;color:var(--red);text-transform:uppercase}
  .lead p{font-size:7.5px;line-height:1.5;margin-top:6px}
  .info{position:absolute;left:18px;right:14px;top:198px}
  .kicker{font-weight:800;font-size:7px;color:var(--red);text-transform:uppercase;letter-spacing:.05em;margin-bottom:7px}
  .ticks{list-style:none}
  .ticks li{display:flex;gap:6px;font-size:7.8px;line-height:1.4;margin-bottom:5px}
  .ticks svg{width:9px;height:9px;flex:none;margin-top:2px}
  .services{position:absolute;left:18px;right:14px;top:395px}
  h3{font-weight:700;font-size:9px;color:var(--navy);line-height:1.25;margin-bottom:4px}
  .body{font-size:7.5px;line-height:1.5}
  .stays{position:absolute;left:20px;right:14px;top:262px}
  .stays section+section{margin-top:11px}
  .reach{position:absolute;left:18px;right:16px;top:268px}
</style>
</head>
<body>

<!-- OUTSIDE SPREAD -->
<div class="spread spread--outside">
  <svg class="spread-art" viewBox="0 0 700 540">
    <defs>
      <linearGradient id="sky" x1="0" y1="0" x2="0" y2="1">
        <stop offset="0" stop-color="#ffffff"/>
        <stop offset=".55" stop-color="#f3ede3"/>
        <stop offset="1" stop-color="#e8dcc7"/>
      </linearGradient>
      <linearGradient id="interior" x1="0" y1="0" x2="1" y2="1">
        <stop offset="0" stop-color="#a8632f"/><stop offset="1" stop-color="#5a2f17"/>
      </linearGradient>
      <linearGradient id="caribou" x1="0" y1="0" x2="1" y2="1">
        <stop offset="0" stop-color="#b58a5a"/><stop offset="1" stop-color="#5d5a4f"/>
      </linearGradient>
      <linearGradient id="sheep" x1="0" y1="0" x2="1" y2="1">
        <stop offset="0" stop-color="#9c9c96"/><stop offset="1" stop-color="#e6e2b4"/>
      </linearGradient>
      <linearGradient id="roof" x1="0" y1="0" x2="1" y2="1">
        <stop offset="0" stop-color="#d8d4cc"/><stop offset="1" stop-color="#4a3a2c"/>
      </linearGradient>
      <linearGradient id="lodge" x1="0" y1="0" x2="0" y2="1">
        <stop offset="0" stop-color="#7fb3e6"/><stop offset=".5" stop-color="#3d3a30"/><stop offset="1" stop-color="#6b6a52"/>
      </linearGradient>
    </defs>
    <rect x="233" y="0" width="467" height="540" fill="url(#sky)"/>
    <!-- left panel art -->
    <polygon points="0,420 70,350 70,540 0,540" fill="var(--red)"/>
    <g role="img" aria-label="Photo of the lodge lounge interior with log walls">
      <rect x="-60" y="-60" width="120" height="120" rx="14" transform="translate(150 470) rotate(45)" fill="url(#interior)"/>
    </g>
    <!-- cover art -->
    <polygon points="490,0 540,0 515,25" fill="var(--orange)"/>
    <g role="img" aria-label="Photo of a caribou bull with antlers">
      <rect x="-40" y="-40" width="80" height="80" rx="11" transform="translate(528 106) rotate(45)" fill="url(#caribou)"/>
    </g>
    <g role="img" aria-label="Photo of a Dall sheep ram">
      <rect x="-40" y="-40" width="80" height="80" rx="11" transform="translate(590 168) rotate(45)" fill="url(#sheep)"/>
    </g>
    <g role="img" aria-label="Photo of the lodge roof and balcony">
      <rect x="-40" y="-40" width="80" height="80" rx="11" transform="translate(528 230) rotate(45)" fill="url(#roof)"/>
    </g>
    <g role="img" aria-label="Photo of the main lodge with mountains behind">
      <rect x="-40" y="-40" width="80" height="80" rx="11" transform="translate(652 230) rotate(45)" fill="url(#lodge)"/>
    </g>
    <polygon points="700,272 666,306 700,340" fill="var(--navy)"/>
  </svg>
  <div class="fold" style="left:233px"></div>
  <div class="fold" style="left:466px"></div>

  <div class="panel panel--left">
    <div class="intro">
      <p>Welcome to Pine Hollow Camp, a place we are proud to call the REAL ALASKA! Take a 30 minute sightseeing flight from Tamarack Flats to the heart of the mountains, landing right on our private airstrip at the base of Mt. Corvane and its wide valley. Enjoy your private cabin with access to the Main Lodge, dining hall and lounge. Tour the many rustic buildings on the premises, including our sauna and trappers cabin, and walk the trails near camp.</p>
      <p>This is truly a wilderness lodge and we invite everyone to partake in the many outdoor activities or simply relax by the fire pit. Canoe the pond, watch for wildlife from the deck, or gaze at Mt. Corvane from the dining room. Start your adventure with Sky Tundrix as they show you glaciers, rivers and wildlife. Our staff will give you a tour of the lodge, the buildings and grounds, and show you to your private cabin.</p>
    </div>
  </div>

  <div class="panel panel--middle">
    <div class="contact-brand"><div class="brand"><span class="brand-dot"></span>Pine Hollow Camp</div></div>
    <div class="contact-card">
      <div class="contact-row">
        <svg viewBox="0 0 24 24"><path fill="#fff" d="M6.6 10.8a15 15 0 0 0 6.6 6.6l2.2-2.2a1 1 0 0 1 1-.25 11.4 11.4 0 0 0 3.6.57 1 1 0 0 1 1 1V20a1 1 0 0 1-1 1A17 17 0 0 1 3 4a1 1 0 0 1 1-1h3.5a1 1 0 0 1 1 1c0 1.25.2 2.45.57 3.57a1 1 0 0 1-.25 1z"/></svg>
        +1 907-555-0148
      </div>
      <div class="contact-row">
        <svg viewBox="0 0 24 24"><circle cx="12" cy="12" r="9" fill="none" stroke="#fff" stroke-width="2"/><path d="M3 12h18M12 3c3 3 3 15 0 18M12 3c-3 3-3 15 0 18" fill="none" stroke="#fff" stroke-width="1.6"/></svg>
        www.pinehollowcamp.com
      </div>
      <div class="contact-row">
        <svg viewBox="0 0 24 24"><path fill="#fff" d="M12 2a7 7 0 0 0-7 7c0 5 7 13 7 13s7-8 7-13a7 7 0 0 0-7-7zm0 9.5A2.5 2.5 0 1 1 12 6.5a2.5 2.5 0 0 1 0 5z"/></svg>
        Pine Hollow Camp Tamarack Flats, Alaska 99790
      </div>
    </div>
  </div>

  <div class="panel panel--right">
    <div class="cover-brand"><div class="brand"><span class="brand-dot"></span>Pine Hollow Camp</div></div>
    <div class="cover-title">
      <div class="title-top">ALASKAN</div>
      <div class="title-main">Wilderness<br>Fly-In Lodge</div>
      <div class="title-sub">Remote property!!<br>There are no roads here!!<br>You must fly!!</div>
    </div>
    <div class="url-bar">www.pinehollowcamp.com</div>
  </div>
</div>

<!-- INSIDE SPREAD -->
<div class="spread spread--inside">
  <svg class="spread-art" viewBox="0 0 700 540">
    <defs>
      <linearGradient id="mount" x1="0" y1="0" x2="0" y2="1">
        <stop offset="0" stop-color="#ffffff"/><stop offset=".5" stop-color="#c9ced6"/><stop offset="1" stop-color="#f4f5f7"/>
      </linearGradient>
      <linearGradient id="cabin" x1="0" y1="0" x2="1" y2="1">
        <stop offset="0" stop-color="#7c9a5a"/><stop offset="1" stop-color="#6a4026"/>
      </linearGradient>
      <linearGradient id="door" x1="0" y1="0" x2="1" y2="1">
        <stop offset="0" stop-color="#8a5632"/><stop offset="1" stop-color="#4a2a18"/>
      </linearGradient>
      <linearGradient id="trophy" x1="0" y1="0" x2="1" y2="1">
        <stop offset="0" stop-color="#6f5a44"/><stop offset="1" stop-color="#3b2a1e"/>
      </linearGradient>
      <linearGradient id="moose" x1="0" y1="0" x2="1" y2="1">
        <stop offset="0" stop-color="#c08a5c"/><stop offset="1" stop-color="#6b3e22"/>
      </linearGradient>
    </defs>
    <g role="img" aria-label="Photo of snowy mountain peaks">
      <rect x="18" y="140" width="200" height="52" fill="url(#mount)"/>
    </g>
    <g role="img" aria-label="Photo of a log guest cabin exterior">
      <rect x="-56" y="-56" width="112" height="112" rx="14" transform="translate(298 62) rotate(45)" fill="url(#cabin)"/>
    </g>
    <g role="img" aria-label="Photo of a wooden cabin doorway">
      <rect x="-56" y="-56" width="112" height="112" rx="14" transform="translate(384 138) rotate(45)" fill="url(#door)"/>
    </g>
    <g role="img" aria-label="Photo of the lodge interior with mounted antlers">
      <rect x="-50" y="-50" width="100" height="100" rx="13" transform="translate(500 30) rotate(45)" fill="url(#trophy)"/>
    </g>
    <g role="img" aria-label="Photo of a moose in the lodge">
      <rect x="-56" y="-56" width="112" height="112" rx="14" transform="translate(620 140) rotate(45)" fill="url(#moose)"/>
    </g>
    <rect x="-40" y="-40" width="80" height="80" rx="10" transform="translate(300 202) rotate(45)" fill="var(--red)"/>
    <text x="300" y="192" text-anchor="middle" font-family="Montserrat, sans-serif" font-weight="800" font-size="7.5" fill="#fff">PRIVATE CABINS</text>
    <text x="300" y="204" text-anchor="middle" font-family="Montserrat, sans-serif" font-weight="800" font-size="7.5" fill="#fff">AND PRIVATE</text>
    <text x="300" y="216" text-anchor="middle" font-family="Montserrat, sans-serif" font-weight="800" font-size="7.5" fill="#fff">BATHROOMS!</text>
  </svg>
  <div class="fold" style="left:233px"></div>
  <div class="fold" style="left:466px"></div>

  <div class="panel panel--left">
    <div class="lead">
      <div class="lead-title">Pine Hollow Camp can accommodate families, large groups, prolonged stays, &amp; custom vacation types.</div>
      <p>Guests have access to the Main Lodge, theater, private cabins, wood fired sauna, trappers cabin museum, lodge grounds, Heron Pond canoe &amp; all of the surrounding public land.</p>
    </div>
    <div class="info">
      <div class="kicker">Information</div>
      <ul class="ticks">
        <li><svg viewBox="0 0 10 10"><circle cx="5" cy="5" r="5" fill="var(--navy)"/><path d="M2.7 5.2l1.6 1.6 3-3.2" fill="none" stroke="#fff" stroke-width="1.2"/></svg>Accommodations include your own private cabin with private bathroom.</li>
        <li><svg viewBox="0 0 10 10"><circle cx="5" cy="5" r="5" fill="var(--navy)"/><path d="M2.7 5.2l1.6 1.6 3-3.2" fill="none" stroke="#fff" stroke-width="1.2"/></svg>Access to the main lodge lounge and dining rooms.</li>
        <li><svg viewBox="0 0 10 10"><circle cx="5" cy="5" r="5" fill="var(--navy)"/><path d="M2.7 5.2l1.6 1.6 3-3.2" fill="none" stroke="#fff" stroke-width="1.2"/></svg>Wood fired sauna.</li>
        <li><svg viewBox="0 0 10 10"><circle cx="5" cy="5" r="5" fill="var(--navy)"/><path d="M2.7 5.2l1.6 1.6 3-3.2" fill="none" stroke="#fff" stroke-width="1.2"/></svg>Covered fire pit, and use of our canoe.</li>
        <li><svg viewBox="0 0 10 10"><circle cx="5" cy="5" r="5" fill="var(--navy)"/><path d="M2.7 5.2l1.6 1.6 3-3.2" fill="none" stroke="#fff" stroke-width="1.2"/></svg>Life jackets, and rubber boots.</li>
        <li><svg viewBox="0 0 10 10"><circle cx="5" cy="5" r="5" fill="var(--navy)"/><path d="M2.7 5.2l1.6 1.6 3-3.2" fill="none" stroke="#fff" stroke-width="1.2"/></svg>Meals available.</li>
        <li><svg viewBox="0 0 10 10"><circle cx="5" cy="5" r="5" fill="var(--navy)"/><path d="M2.7 5.2l1.6 1.6 3-3.2" fill="none" stroke="#fff" stroke-width="1.2"/></svg>Wifi in main lodge.</li>
      </ul>
    </div>
    <div class="services">
      <div class="kicker">Services</div>
      <h3>Hiking 10 local trails</h3>
      <p class="body">All trails begin at the lodge. Take Fernwood trail to the boreal forest for bird and wildlife watching. Hike to Heron Pond or Loon Pond. Climb the trail up Mt. Corvane and view the Dall Sheep. Take Slate Knob trail for a hike above the trees. Many more. Rubber boots, bear spray, maps.</p>
    </div>
  </div>

  <div class="panel panel--middle">
    <div class="stays">
      <section>
        <h3>Nightly Bed and Breakfast in our Cabins</h3>
        <p class="body">Stay in one of our private cabins with private bathroom, hot water, baseboard heat or wood stove for $150/night. Most rooms have a queen and a twin bed. Breakfast included. Optional lunch and dinner at $20/person.</p>
      </section>
      <section>
        <h3>Flight Seeing trips</h3>
        <p class="body">Take a Kestrel 6 or Turbo Otterline from Tamarack Flats across glaciers, mountains, rivers, lakes and myriad wildlife. Land at Pine Hollow Camp and stay as many days as you like. Then take another route back to the airport for your outbound trip. $300 each way, or book the plane for $650 each way.</p>
      </section>
      <section>
        <h3>Canoeing on Heron Pond!</h3>
        <p class="body">Paddle our canoe around Heron Pond. Photograph the swans, ducks, or other wildlife. Canoe, paddles, life jackets, rubber boots provided.</p>
      </section>
    </div>
  </div>

  <div class="panel panel--right">
    <div class="reach">
      <div class="kicker">How to reach</div>
      <p class="body">From Tamarack Flats airport, Sky Tundrix will take you on a 30 minute scenic tour of mountains, glaciers and wildlife. Upon arrival at Pine Hollow Camp, our staff will greet you and give you a tour of the property, shown to the main lodge, then show you to your private cabin. Guests may explore the grounds, with historic cabins and a private sauna. Breakfast is served in the lodge, and guests can hike, fish, canoe, take a boat to Heron Pond, go for a long trek, hike Mt. Corvane, pan for gold in the creeks, and much more!</p>
    </div>
  </div>
</div>

</body>
</html>
```